Highly rated moving company needs postcard design

We need a highly converting postcard to send when people put their homes for sale online. This should highlight the fact that we're Austin's highest rated moving company, and should convey quality and value. We do local, statewide and long distance moves. We also do office and commerical moves and storage. final design must be sized to work with our mailing system. Please see attached file for more information.

```html
<!DOCTYPE html>
<html lang="en">
<head>
<meta charset="utf-8">
<title>Ridgeline Movers Postcard</title>
<link rel="stylesheet" href="https://fonts.googleapis.com/css2?family=Montserrat:wght@400;600;700;800&family=Open+Sans:wght@400;600&display=swap">
<style>
  :root {
    --backdrop: #3b2342;
    --card-white: #ffffff;
    --brand-red: #e0141e;
    --brand-navy: #27237a;
    --tone-blue: #3f4f9c;
    --tone-lilac: #8a84b8;
    --tone-warm: #c98f6e;
    --tone-dusk: #3a2f44;
    --cream: #efe6d4;
    --cream-edge: #e4d8bf;
    --ink: #2b2320;
    --rule: #6b4a3a;
    --label: #b98a4a;
  }
  * { box-sizing: border-box; margin: 0; padding: 0; }
  html, body { width: 1200px; height: 944px; overflow: hidden; }
  body {
    background: var(--backdrop);
    font-family: "Open Sans", sans-serif;
    position: relative;
  }

  /* ---------- Front of card ---------- */
  .postcard-front {
    position: absolute;
    left: 280px; top: 28px;
    width: 640px; height: 430px;
    background: var(--card-white);
    padding: 14px;
  }
  .front-photo {
    position: relative;
    width: 100%; height: 100%;
    background: linear-gradient(165deg, var(--tone-blue) 0%, var(--tone-lilac) 45%, var(--tone-warm) 72%, var(--tone-dusk) 100%);
    overflow: hidden;
  }
  .front-photo .scene {
    position: absolute; inset: 0;
  }
  .front-headline {
    position: absolute;
    right: 26px; top: 26px;
    text-align: right;
    color: var(--card-white);
    font-family: "Montserrat", sans-serif;
  }
  .front-headline .tagline {
    font-weight: 800;
    font-size: 30px;
    line-height: 1;
    letter-spacing: .5px;
  }
  .front-headline .tagline .line-two { font-size: 36px; display: block; }
  .front-headline .city {
    font-weight: 700;
    font-size: 24px;
    margin-top: 8px;
  }
  .front-headline .blurb {
    font-family: "Open Sans", sans-serif;
    color: var(--brand-navy);
    font-size: 11.5px;
    line-height: 1.35;
    margin-top: 8px;
  }
  .brand-box {
    position: absolute;
    right: 26px; top: 206px;
    width: 196px; height: 106px;
    padding: 10px 12px;
    background: var(--card-white);
    display: flex; flex-direction: column;
    align-items: center; justify-content: center;
    gap: 10px;
    text-align: center;
  }
  .brand-dot {
    width: 34px; height: 34px;
    border-radius: 50%;
    background: var(--brand-navy);
  }
  .brand-name {
    font-family: "Montserrat", sans-serif;
    font-weight: 800;
    color: var(--brand-red);
    font-size: 15px;
    letter-spacing: .5px;
    text-transform: uppercase;
    white-space: nowrap;
  }
  .front-web {
    position: absolute;
    right: 26px; top: 320px;
    color: var(--card-white);
    font-size: 11.5px;
  }
  .service-list {
    position: absolute;
    right: 22px; bottom: 14px;
    display: flex; gap: 8px;
    list-style: none;
    font-family: "Montserrat", sans-serif;
    color: var(--card-white);
    font-size: 9px;
    letter-spacing: .6px;
    text-transform: uppercase;
  }
  .service-list li + li::before {
    content: "|";
    color: var(--brand-red);
    margin-right: 8px;
  }

  /* ---------- Back of card ---------- */
  .postcard-back {
    position: absolute;
    left: 280px; top: 486px;
    width: 640px; height: 430px;
    background: linear-gradient(135deg, var(--cream) 0%, var(--cream-edge) 100%);
    padding: 14px;
  }
  .back-frame {
    position: relative;
    width: 100%; height: 100%;
    border: 4px solid #b7c9b6;
    outline: 4px solid #d9b47a;
    outline-offset: -12px;
  }
  .sender-block {
    position: absolute;
    left: 30px; top: 80px;
    width: 270px;
    text-align: center;
    color: var(--ink);
  }
  .sender-block .brand-dot { display: block; margin: 0 auto 10px; width: 46px; height: 46px; }
  .sender-block .brand-name { font-size: 22px; }
  .sender-copy {
    margin-top: 18px;
    font-size: 12.5px;
    line-height: 1.45;
  }
  .divider {
    position: absolute;
    left: 318px; top: 40px; bottom: 50px;
    width: 1px;
    background: var(--rule);
  }
  .stamp-box {
    position: absolute;
    right: 36px; top: 36px;
    width: 74px; height: 88px;
    border: 1.5px dashed #c2a27b;
  }
  .address-block {
    position: absolute;
    left: 344px; right: 36px; top: 170px;
  }
  .address-line {
    border-bottom: 1px solid var(--rule);
    height: 36px;
    display: flex; align-items: flex-end;
    padding-bottom: 4px;
    font-size: 12px;
    color: var(--ink);
  }
  .address-line .to-label {
    color: var(--label);
    margin-right: 12px;
  }
</style>
</head>
<body>

  <section class="postcard-front" aria-label="Postcard front">
    <div class="front-photo">
      <div class="scene" role="img" aria-label="Photo of a moving truck driving down a highway at sunset"></div>

      <div class="front-headline">
        <h1 class="tagline">LET OUR FAMILY <span class="line-two">MOVE YOURS</span></h1>
        <p class="city">Austin Movers</p>
        <p class="blurb">Austinites rave about our moving help.<br>We’re proud to be the most dependable<br>moving company in Austin.</p>
      </div>

      <div class="brand-box">
        <span class="brand-dot"></span>
        <span class="brand-name">Ridgeline Movers</span>
      </div>
      <p class="front-web">www.ridgelinemoversatx.com</p>

      <ul class="service-list">
        <li>Local Moves</li>
        <li>Long Distance</li>
        <li>Residential</li>
        <li>Commercial</li>
        <li>Packing Services</li>
      </ul>
    </div>
  </section>

  <section class="postcard-back" aria-label="Postcard back">
    <div class="back-frame">
      <div class="sender-block">
        <span class="brand-dot"></span>
        <p class="brand-name">Ridgeline Movers</p>
        <p class="sender-copy">
          Lorem ipsum dolor sit amet, consectetuer<br>
          adipiscing elit, sed diam nonummy<br>
          nibh euismod tincidunt ut l<br>
          Tele : 512-555-0148<br>
          www.ridgelinemoversatx.com
        </p>
      </div>

      <div class="divider"></div>
      <div class="stamp-box"></div>

      <div class="address-block">
        <p class="address-line"><span class="to-label">TO:</span>Lorem ipsum dolor sit</p>
        <p class="address-line">Lorem ipsum dolor sit Lorem ipsum</p>
        <p class="address-line"></p>
        <p class="address-line"></p>
      </div>
    </div>
  </section>

</body>
</html>
```